Business Card Design

I already have a company logo for my company. I have a logo for the manufacturer we represent. I want a professional business card design.

```html
<!DOCTYPE html>
<html lang="en">
<head>
<meta charset="utf-8">
<title>Signal Crest LLC – Business Card</title>
<link rel="stylesheet" href="https://fonts.googleapis.com/css2?family=Open+Sans:wght@400;600;700&display=swap">
<style>
  :root {
    --stage: #3b3b3b;
    --card-black: #0b0b0b;
    --card-white: #ffffff;
    --brand-red: #e21f26;
    --brand-gold: #a8822a;
    --text-light: #f2f2f2;
  }
  * { box-sizing: border-box; margin: 0; padding: 0; }
  html, body { width: 1200px; height: 780px; overflow: hidden; }
  body {
    background: var(--stage);
    font-family: "Open Sans", Arial, sans-serif;
    position: relative;
  }
  .card {
    position: absolute;
    top: 235px;
    width: 540px;
    height: 310px;
    border-radius: 18px;
    overflow: hidden;
    box-shadow: 0 14px 30px rgba(0,0,0,.45);
  }
  .card--front { left: 40px; background: var(--card-black); }
  .card--back { left: 620px; background: var(--card-black); }
  .card__art { position: absolute; inset: 0; width: 100%; height: 100%; }

  .brand {
    position: absolute;
    display: flex;
    align-items: center;
    gap: 10px;
    color: var(--brand-red);
    font-weight: 700;
    letter-spacing: 1px;
    text-transform: uppercase;
    white-space: nowrap;
  }
  .brand__mark { width: 22px; height: 22px; background: var(--brand-red); }
  .card--front .brand { left: 210px; top: 52px; font-size: 20px; }
  .card--back .brand { left: 50%; top: 50%; transform: translate(-50%, -50%); font-size: 34px; }
  .card--back .brand__mark { width: 40px; height: 40px; border-radius: 50%; }

  .person { position: absolute; left: 50px; top: 176px; }
  .person__name { color: var(--brand-red); font-size: 17px; font-weight: 600; text-transform: uppercase; letter-spacing: .5px; line-height: 22px; }
  .person__title { color: var(--text-light); font-size: 13px; margin-top: 2px; }

  .divider { position: absolute; left: 252px; top: 188px; width: 1.5px; height: 62px; background: var(--brand-red); }

  .contacts { position: absolute; left: 268px; top: 186px; list-style: none; }
  .contacts li { display: flex; align-items: center; gap: 7px; color: var(--text-light); font-size: 12.5px; line-height: 16px; }
  .contacts svg { width: 11px; height: 11px; fill: var(--brand-red); flex: none; }

  .website {
    position: absolute; left: 0; right: 0; bottom: 0; height: 40px;
    display: flex; align-items: center; padding-left: 140px;
    color: var(--text-light); font-size: 14px;
  }
</style>
</head>
<body>

<section class="card card--front" aria-label="Business card front">
  <svg class="card__art" viewBox="0 0 540 310" preserveAspectRatio="none" aria-hidden="true">
    <path d="M0,0 L540,0 L540,130 C330,180 110,170 0,20 Z" fill="var(--card-white)"/>
    <path d="M0,20 C110,170 330,180 540,130 L540,152 C330,200 100,190 0,46 Z" fill="var(--brand-red)"/>
    <path d="M30,0 C120,148 330,166 540,120" fill="none" stroke="var(--brand-gold)" stroke-width="2"/>
    <rect x="0" y="267" width="540" height="3" fill="var(--brand-gold)"/>
    <rect x="0" y="270" width="540" height="40" fill="var(--brand-red)"/>
  </svg>

  <div class="brand"><span class="brand__mark"></span>Signal Crest LLC</div>

  <div class="person">
    <p class="person__name">Daniel Hart</p>
    <p class="person__title">Managing Director</p>
  </div>

  <span class="divider"></span>

  <ul class="contacts">
    <li><svg viewBox="0 0 24 24"><path d="M6.6 10.8a15 15 0 0 0 6.6 6.6l2.2-2.2a1 1 0 0 1 1-.25 11.4 11.4 0 0 0 3.6.57 1 1 0 0 1 1 1V20a1 1 0 0 1-1 1A17 17 0 0 1 3 4a1 1 0 0 1 1-1h3.5a1 1 0 0 1 1 1c0 1.25.2 2.45.57 3.57a1 1 0 0 1-.25 1z"/></svg>555 014 2738</li>
    <li><svg viewBox="0 0 24 24"><path d="M6 2h12v6H6zM3 9h18v9h-3v4H6v-4H3zm5 7v4h8v-4z"/></svg>555 014 2739</li>
    <li><svg viewBox="0 0 24 24"><path d="M7 1h10a2 2 0 0 1 2 2v18a2 2 0 0 1-2 2H7a2 2 0 0 1-2-2V3a2 2 0 0 1 2-2zm0 3v14h10V4z"/></svg>555 014 2740</li>
    <li><svg viewBox="0 0 24 24"><path d="M2 5h20v14H2zm2 2v.5l8 5 8-5V7l-8 5z"/></svg>info@signalcrest.com</li>
  </ul>

  <p class="website">www.signalcrest.com</p>
</section>

<section class="card card--back" aria-label="Business card back">
  <div class="brand"><span class="brand__mark"></span>Signal Crest LLC</div>
</section>

</body>
</html>
```